Velmora Supply Chain and Logistic Consulting

Please review the attached Business Card. I want as close to this card with the colors, fonts, and quality of the card as possible. The attached compass should replace the deer head on both sides of the card and the text should say:

Backside
Compass JPEG
Velmora Logistics
A Supply Chain and Logistics Consulting Company

Frontside
Velmora Logistics
Ravi Ostrander - Marlow Bay Oregon
President
____________________________________
(362) 555-0193
Velmora@Quillpost.com
_____________________________________

Bottom Front Side

Target Market(s)

Businesses

Contact Information for Business Card

Backside
Compass JPEG
Velmora Logistics

Frontside
Velmora Logistics
President
(362) 555-0193
Velmora@Quillpost.com

Bottom Front Side

Font styles to use
Serif
Script

Colors

Designer to choose colors to be used in the design.

Requirements
Must have
• See attached card for reference
Nice to have
Should not have

```html
<!DOCTYPE html>
<html lang="en">
<head>
<meta charset="utf-8">
<title>Velmora Logistics — Business Card</title>
<link rel="stylesheet" href="https://fonts.googleapis.com/css2?family=Tinos&display=swap">
<style>
  :root {
    --stage: #141414;
    --card: #2a2a2a;
    --card-edge: #1d1d1d;
    --ink: #f2f2f2;
    --ink-soft: #cfcfcf;
    --rule: #bdbdbd;
    --mark: #8a8a8a;
  }
  * { box-sizing: border-box; margin: 0; padding: 0; }
  html, body {
    width: 1200px; height: 900px; overflow: hidden;
    background: var(--stage);
  }
  .stage {
    width: 1200px; height: 900px;
    display: flex; align-items: center; justify-content: center; gap: 40px;
  }
  .card {
    width: 540px; height: 310px;
    background: var(--card);
    border: 1px solid var(--card-edge);
    box-shadow: 0 14px 30px rgba(0,0,0,.6);
    position: relative;
    display: flex; flex-direction: column; align-items: center; justify-content: center;
    color: var(--ink);
    font-family: "Tinos", "Times New Roman", serif;
    text-align: center;
  }
  .brand-name {
    font-family: "Tinos", "Times New Roman", serif;
    font-weight: 400;
    color: var(--ink);
    line-height: 1;
  }
  .tagline { color: var(--ink-soft); }

  /* Front */
  .card-front .brand-name { font-size: 30px; }
  .card-front .tagline { font-size: 13px; margin-top: 5px; }
  .card-front .person { font-size: 17px; margin-top: 12px; }
  .card-front .role { font-size: 15px; margin-top: 2px; }
  .card-front .rule { width: 300px; height: 1px; background: var(--rule); margin: 10px 0; }
  .card-front .contact { font-size: 15px; line-height: 1.35; }
  .card-front .tagline-foot { font-size: 13px; margin-top: 2px; }
  .card-front .rule-long { width: 380px; }

  /* Back */
  .card-back .mark {
    width: 84px; height: 84px; border-radius: 50%;
    background: var(--mark);
    margin-bottom: 16px;
  }
  .card-back .brand-name { font-size: 30px; }
  .card-back .tagline { font-size: 13px; margin-top: 6px; }
</style>
</head>
<body>
<main class="stage">
  <section class="card card-front" aria-label="Business card front">
    <h1 class="brand-name">Velmora Logistics</h1>
    <p class="tagline">A Supply Chain and Logistics Consulting Company</p>
    <p class="person">Ravi Ostrander &bull; Marlow Bay Oregon</p>
    <p class="role">President</p>
    <div class="rule"></div>
    <p class="contact">(362) 555-0193<br>Velmora@Quillpost.com</p>
    <div class="rule"></div>
    <p class="tagline tagline-foot">A Supply Chain and Logistics Consulting Company</p>
    <div class="rule rule-long"></div>
  </section>

  <section class="card card-back" aria-label="Business card back">
    <div class="mark" aria-hidden="true"></div>
    <h2 class="brand-name">Velmora Logistics</h2>
    <p class="tagline">A Supply Chain and Logistics Consulting Company</p>
  </section>
</main>
</body>
</html>
```